Business Cards for accounting firm

Need a file and design that we can update for our employees when we get a design we like. Logo is attached.
Megan Tolliver CPA
Owner
P.O. Box 418
Perrysburg OH 43187
4193628405
megan@brightlanefin.com
www.brightlanefin.com
Accounting

```html
<!DOCTYPE html>
<html lang="en">
<head>
<meta charset="UTF-8">
<title>Brightlane Financial – Business Cards</title>
<link href="https://fonts.googleapis.com/css2?family=Source+Sans+3:wght@400;600;700&display=swap" rel="stylesheet">
<style>
  :root {
    --backdrop: #e4e4e4;
    --card: #f7f7f6;
    --ink-gray: #5f5f5f;
    --brand-blue: #1f9ad6;
    --card-shadow: rgba(0, 0, 0, 0.16);
  }
  * { box-sizing: border-box; margin: 0; padding: 0; }
  html, body {
    width: 1200px;
    height: 900px;
    overflow: hidden;
    background: var(--backdrop);
    font-family: "Source Sans 3", "Myriad Pro", Arial, sans-serif;
  }
  .canvas {
    position: relative;
    width: 1200px;
    height: 900px;
  }
  .card {
    position: absolute;
    width: 504px;
    height: 288px;
    background: var(--card);
    box-shadow: 0 10px 24px var(--card-shadow);
  }
  .card--front { left: 110px; top: 470px; }
  .card--back  { left: 590px; top: 150px; }

  /* Front: centred brand name */
  .front-brand {
    position: absolute;
    inset: 0;
    display: flex;
    align-items: center;
    justify-content: center;
    gap: 14px;
  }
  .front-brand__mark {
    width: 30px;
    height: 30px;
    border-radius: 50%;
    background: var(--brand-blue);
  }
  .front-brand__name {
    color: var(--brand-blue);
    font-weight: 700;
    font-size: 40px;
    letter-spacing: -0.5px;
  }

  /* Back: contact details */
  .contact {
    position: absolute;
    left: 34px;
    top: 150px;
  }
  .contact__name {
    color: var(--ink-gray);
    font-size: 27px;
    font-weight: 400;
    line-height: 1;
  }
  .contact__role {
    color: var(--brand-blue);
    font-size: 10px;
    margin-top: 4px;
  }
  .contact__details {
    list-style: none;
    margin-top: 9px;
    color: var(--brand-blue);
    font-size: 10.5px;
    line-height: 1.1;
  }
  .back-brand {
    position: absolute;
    right: 26px;
    bottom: 38px;
    display: flex;
    align-items: center;
    gap: 7px;
  }
  .back-brand__mark {
    width: 14px;
    height: 14px;
    border-radius: 50%;
    background: var(--brand-blue);
  }
  .back-brand__name {
    color: var(--brand-blue);
    font-weight: 700;
    font-size: 19px;
  }
</style>
</head>
<body>
<main class="canvas">
  <section class="card card--front" aria-label="Card front">
    <div class="front-brand">
      <span class="front-brand__mark"></span>
      <span class="front-brand__name">Brightlane Financial</span>
    </div>
  </section>

  <section class="card card--back" aria-label="Card back">
    <div class="contact">
      <h1 class="contact__name">Megan Tolliver CPA</h1>
      <p class="contact__role">Owner</p>
      <ul class="contact__details">
        <li>P.O. Box 418</li>
        <li>Harlow Creek KS 43187</li>
        <li>5553628405</li>
        <li>megan@brightlanefin.com</li>
        <li>www.brightlanefin.com</li>
      </ul>
    </div>
    <div class="back-brand">
      <span class="back-brand__mark"></span>
      <span class="back-brand__name">Brightlane Financial</span>
    </div>
  </section>
</main>
</body>
</html>
```